Qb Panes

We need a website design for a company based in Texas that specializes in doors and and windows.
Qb Pane is a leading window manufacturer of aluminum and vinyl windows, both serving the replacement and new construction markets. Qb Pane Inc. was created over 25 years ago when two existing window manufacturers with excellent reputations in their fields - merged. Qb Pane offers a complete line conforming to the needs of residential and commercial window markets.
The final design should be something that communicates professionalism and features they're key value propositions.
Example websites we like:
http://layouts.pebblecraft.example/zx/satchel/
http://layouts.pebblecraft.example/zx/splashyard/
http://layouts.pebblecraft.example/zx/rebuildr2/
This design should format the existing content to be more visually organized, improve the fonts to clearer and more readable, and make it easier for users to find services.
Brand guide is attached
Website images can be found here: https://docs.vaultcrate.example/7kRTmwQzLpXeBd
Target Market(s)
Windows
Number of Pages Required
1 page
Look and feel
Each slider illustrates characteristics of the customer's brand and the style your logo design should communicate.

```html
<!DOCTYPE html>
<html lang="en">
<head>
<meta charset="utf-8">
<title>Qb Pane — Windows, Doors &amp; Sunrooms</title>
<link href="https://fonts.googleapis.com/css2?family=Roboto:ital,wght@0,400;0,500;0,700;0,900;1,400&family=Roboto+Condensed:wght@700&family=Permanent+Marker&display=swap" rel="stylesheet">
<style>
:root{
  --maroon:#9c2440;
  --maroon-dark:#8a1f38;
  --gold:#f5b400;
  --orange-line:#e9a21b;
  --ink:#222;
  --text:#444;
  --muted:#888;
  --line:#ddd;
  --grey-band:#ebebeb;
  --footer:#262626;
  --footer-text:#9a9a9a;
  --white:#fff;
}
*{box-sizing:border-box;margin:0;padding:0}
html,body{width:1200px;height:2799px;overflow:hidden}
body{font-family:"Roboto",Arial,sans-serif;color:var(--text);background:var(--white);position:relative}
.abs{position:absolute}

/* header */
.site-header{position:absolute;top:0;left:0;width:1200px;height:78px;border-top:4px solid var(--orange-line);background:var(--white)}
.brand{position:absolute;left:172px;top:18px;display:flex;align-items:center;gap:10px}
.brand-dot{width:16px;height:16px;border-radius:50%;background:var(--gold)}
.brand-name{font-family:"Roboto",Arial,sans-serif;font-weight:500;font-size:36px;color:var(--maroon);letter-spacing:.5px}
.main-nav{position:absolute;right:172px;top:33px;display:flex;gap:18px;font-size:12.5px;font-weight:500;color:var(--ink);text-transform:uppercase}
.main-nav .active{color:var(--maroon)}

/* hero */
.hero{position:absolute;top:78px;left:0;width:1200px;height:519px;background:linear-gradient(100deg,#b9b2a6 0%,#e9e6df 22%,#8a9a7a 40%,#8fb4d6 60%,#6f9a5a 85%,#5d8a46 100%)}
.hero-copy{position:absolute;right:183px;top:192px;text-align:right;color:var(--white);text-shadow:0 1px 3px rgba(0,0,0,.35)}
.hero-kicker{font-family:"Roboto Condensed",Arial,sans-serif;font-size:23px;text-transform:uppercase}
.hero-sub{font-size:18px;margin-top:2px}
.hero-tagline{font-family:"Permanent Marker",cursive;font-size:27px;margin-top:12px;letter-spacing:1px}

/* products */
.product{position:absolute;top:632px;width:416px;text-align:center}
.product h2{font-family:"Roboto Condensed",Arial,sans-serif;font-size:26px;color:var(--ink);height:44px}
.product-photo{width:416px;height:214px}
.product p{font-size:11.5px;line-height:16px;margin-top:12px;color:var(--text)}
.btn-solid{display:inline-block;margin-top:20px;width:148px;height:38px;line-height:38px;background:var(--maroon);color:var(--white);font-size:12px;font-weight:700;text-transform:uppercase}

/* quote */
.quote{position:absolute;top:1058px;left:0;width:1200px;height:504px;background:linear-gradient(90deg,#9c8878 0%,#cfc2b4 30%,#e9e6e2 55%,#f3f2f0 100%)}
.quote-box{position:absolute;left:685px;top:39px;width:343px;height:422px;background:var(--maroon);padding:28px 50px;text-align:center;color:var(--white)}
.quote-box h2{font-family:"Roboto Condensed",Arial,sans-serif;font-size:31px}
.quote-box .lead{font-size:10.5px;font-weight:700;text-transform:uppercase;margin-top:2px}
.field{background:var(--white);border-radius:3px;height:37px;margin-top:8px;text-align:left;color:var(--muted);font-size:10.5px;padding:12px 11px}
.field:first-of-type{margin-top:18px}
.field.msg{height:94px}
.btn-submit{margin-top:14px;height:46px;line-height:46px;background:var(--gold);color:var(--ink);font-family:"Roboto Condensed",Arial,sans-serif;font-size:23px;border-radius:2px}

/* services */
.section-title{position:absolute;top:1603px;left:452px;width:296px;text-align:center;border-bottom:1px solid var(--line);padding-bottom:12px}
.section-title h2{font-family:"Roboto Condensed",Arial,sans-serif;font-size:27px;color:var(--ink)}
.section-title::after{content:"";position:absolute;left:123px;bottom:-3px;width:50px;height:5px;background:var(--maroon)}
.service{position:absolute;top:1694px;width:198px;height:267px;border:1px solid var(--line);text-align:center}
.service-photo{height:135px}
.service h3{font-family:"Roboto Condensed",Arial,sans-serif;font-size:17px;color:var(--maroon);margin-top:9px;text-transform:uppercase}
.service p{font-size:11px;line-height:15px;padding:0 16px;margin-top:2px}
.btn-outline{display:inline-block;margin-top:11px;width:80px;height:26px;line-height:24px;border:1px solid #aaa;font-size:9.5px;text-transform:uppercase;color:var(--text)}

.partner{position:absolute;top:2011px;width:198px;height:92px;border:1px solid var(--line);display:flex;align-items:center;justify-content:center;gap:8px}
.partner-name{font-size:24px;font-weight:500;color:#555}
.badge-blue{width:144px;height:64px;background:#1a7fc4}
.badge-square{width:56px;height:64px;background:var(--maroon);border:3px solid #e5c7cf}

/* testimonial */
.testimonial{position:absolute;top:2163px;left:0;width:1200px;height:347px;background:var(--grey-band);text-align:center}
.avatar{position:absolute;left:546px;top:32px;width:104px;height:104px;border-radius:50%;border:3px solid var(--white);box-shadow:0 0 0 1px #bbb;background:linear-gradient(#6b5a4c,#c9b3a1)}
.testimonial blockquote{position:absolute;left:196px;top:160px;width:808px;font-style:italic;font-size:11px;line-height:18px;color:#555}
.dots{position:absolute;top:222px;left:0;width:1200px;font-size:18px;letter-spacing:4px;color:#444}
.author{position:absolute;top:252px;left:0;width:1200px;font-size:11px;text-transform:uppercase;color:#444}
.social{position:absolute;top:284px;left:518px;display:flex;gap:10px}
.social span{width:24px;height:24px;border:1px solid #888;border-radius:50%}

/* footer */
.site-footer{position:absolute;top:2510px;left:0;width:1200px;height:289px;background:var(--footer);color:var(--footer-text)}
.footer-col{position:absolute;top:52px}
.footer-col h4{font-size:12.5px;font-weight:500;color:#ccc;text-transform:uppercase;margin-bottom:10px}
.footer-col li{list-style:none;font-size:11px;line-height:20px}
.footer-col li::before{content:"▸ ";font-size:9px}
.copyright{position:absolute;left:175px;top:250px;font-size:10.5px}
.footer-social{position:absolute;right:187px;top:245px;display:flex;gap:10px}
.footer-social span{width:24px;height:24px;border:1px solid #777;border-radius:50%}
</style>
</head>
<body>

<header class="site-header">
  <div class="brand"><span class="brand-dot"></span><span class="brand-name">Qb Pane</span></div>
  <nav class="main-nav">
    <span class="active">Home</span><span>Our Company</span><span>Knowledge Center</span><span>Windows</span><span>Doors</span><span>Sunrooms</span><span>Contact Us</span>
  </nav>
</header>

<section class="hero" role="img" aria-label="Sunlit room with floor-to-ceiling glass walls, a lounge chair on a rug, overlooking a green lawn, lake and mountains">
  <div class="hero-copy">
    <div class="hero-kicker">Beautiful, Energy Efficient,</div>
    <div class="hero-sub">Custom Windows &amp; Doors</div>
    <div class="hero-tagline">QB MAKES IT EASY.</div>
  </div>
</section>

<article class="product" style="left:172px">
  <h2>WINDOWS</h2>
  <div class="product-photo" role="img" aria-label="Bright room with large white-framed windows looking onto trees" style="background:linear-gradient(135deg,#f3f1ec,#c9cfb9 55%,#8f9a6c)"></div>
  <p>Lorem Ipsum is simply dummy text of the printing and typesetting industry. Lorem Ipsum survived not only five centuries, but also the leap into electronic typesetting, remaining essentially unchanged text.</p>
  <span class="btn-solid">See All Collection</span>
</article>
<article class="product" style="left:612px">
  <h2>DOORS</h2>
  <div class="product-photo" role="img" aria-label="Living room with white sofa, rug and glass patio doors" style="background:linear-gradient(135deg,#e9e2d6,#f4f1ec 50%,#b98a6a)"></div>
  <p>Lorem Ipsum is simply dummy text of the printing and typesetting industry. Lorem Ipsum survived not only five centuries, but also the leap into electronic typesetting, remaining essentially unchanged text.</p>
  <span class="btn-solid">See All Collection</span>
</article>

<section class="quote" role="img" aria-label="Smiling senior couple embracing in a bright home">
  <form class="quote-box">
    <h2>GET A FREE QUOTE</h2>
    <div class="lead">Lorem ipsum dolor sit amet mattis.</div>
    <div class="field">Enter your name</div>
    <div class="field">Enter your email ID</div>
    <div class="field">Enter your phone</div>
    <div class="field msg">Enter your message</div>
    <div class="btn-submit">SUBMIT NOW!</div>
  </form>
</section>

<div class="section-title"><h2>OUR SERVICES AREA</h2></div>

<article class="service" style="left:172px">
  <div class="service-photo" role="img" aria-label="Two-storey stone and siding house" style="background:linear-gradient(#9fb7cf,#8a7660 60%,#5f7a3f)"></div>
  <h3>Windows</h3><p>Lorem Ipsum is simply dummy text industry is standard dummy good type specimen book.</p><span class="btn-outline">Read More</span>
</article>
<article class="service" style="left:392px">
  <div class="service-photo" role="img" aria-label="Living room with fireplace and tall windows" style="background:linear-gradient(135deg,#d9cdb9,#6a5a48 60%,#3b3128)"></div>
  <h3>Doors</h3><p>Lorem Ipsum is simply dummy text industry is standard dummy good type specimen book.</p><span class="btn-outline">Read More</span>
</article>
<article class="service" style="left:611px">
  <div class="service-photo" role="img" aria-label="Glass sunroom overlooking a green field" style="background:linear-gradient(#eef0e8,#b8c99a 60%,#8a9a62)"></div>
  <h3>Sunrooms</h3><p>Lorem Ipsum is simply dummy text industry is standard dummy good type specimen book.</p><span class="btn-outline">Read More</span>
</article>
<article class="service" style="left:830px">
  <div class="service-photo" role="img" aria-label="Covered patio with garden and glass doors" style="background:linear-gradient(135deg,#7d8f5a,#d8d4cc 60%,#f1efe9)"></div>
  <h3>Eco Rated</h3><p>Lorem Ipsum is simply dummy text industry is standard dummy good type specimen book.</p><span class="btn-outline">Read More</span>
</article>

<div class="partner" style="left:172px"><span class="partner-name">Huelane</span></div>
<div class="partner" style="left:392px"><span class="partner-name">Solvara</span></div>
<div class="partner" style="left:611px"><span class="badge-blue" aria-label="Efficiency partner badge"></span></div>
<div class="partner" style="left:830px"><span class="badge-square" aria-label="Company badge"></span></div>

<section class="testimonial">
  <div class="avatar" role="img" aria-label="Portrait of the reviewer"></div>
  <blockquote>Lorem Ipsum is simply dummy text of the printing and typesetting industry. Lorem Ipsum has been the industry's standard dummy text ever since the 1500s, when an unknown printer took a galley of type and scrambled it to make a type specimen book. It has survived not only five centuries, but also the leap into electronic typesetting, remaining essentially unchanged.</blockquote>
  <div class="dots">••••</div>
  <div class="author">John Doe</div>
  <div class="social"><span></span><span></span><span></span><span></span><span></span></div>
</section>

<footer class="site-footer">
  <div class="footer-col" style="left:172px"><h4>About Qb Pane</h4><ul><li>Press Releases</li><li>Our Community</li><li>Careers</li><li>Credentials &amp; Awards</li></ul></div>
  <div class="footer-col" style="left:420px"><h4>Our Products</h4><ul><li>Vinyl Windows</li><li>Aluminum Windows</li><li>Doors</li><li>Storm</li><li>Find Windows by Style</li><li>Locate a Dealer</li></ul></div>
  <div class="footer-col" style="left:666px"><h4>Learn About</h4><ul><li>Eco Rated</li><li>Replacement Windows</li><li>New Construction Windows</li><li>Knowledge Center</li></ul></div>
  <div class="footer-col" style="left:935px"><h4>Contact Us</h4><ul><li>Find a Dealer</li><li>Privacy Policy</li><li>Request Service</li></ul></div>
  <div class="copyright">© 2018 All Rights Reserved</div>
  <div class="footer-social"><span></span><span></span><span></span><span></span></div>
</footer>

</body>
</html>
```